Corvella Web Design Project

I am attaching my logo so I need to see applied to the website developed by you guys!!
Tbahks!!
Marcello
This is the DNA of the company
Flat and dynamic organization - Informal and respectful social approac
Innovative - Always striving for the best solution
Reliability and Quality - The value of our name
Flexibility - Ability to handle new requirements and unforeseen events
Simplicity - Technology must serve – NOT rule!
Cooperative Relations - The synergy that makes 1+1=3
We still don´t have our logo as we have another open project on artbazaar
Our company won´t be selling this equipment but providing welding services for shipyard industry, as you can see on the website below.
www.velmorix.com
Updates
Project Deadline Extended
Reason: Hi webdesigners,
I will be deciding my logo by this weekend as soon as I have decided I will post my logo to see it applied to your design!!!
Thanks
Marcello
I just Sent my logo for your attention!!!!
Industry/Entity Type
Welding
Look and feel
Each slider illustrates characteristics of the customer's brand and the style your logo design should communicate.

```html
<!DOCTYPE html>
<html lang="en">
<head>
<meta charset="utf-8">
<title>Corvella – Robotic Welding Technologie</title>
<link href="https://fonts.googleapis.com/css2?family=Lato:wght@300;400;700;900&family=Arimo:wght@400&display=swap" rel="stylesheet">
<style>
:root{
  --orange:#f15a29;
  --orange-soft:#f58a66;
  --ink:#222;
  --text:#333;
  --muted:#666;
  --charcoal:#3d3d3f;
  --frame:#c9c9c9;
  --white:#fff;
}
*{margin:0;padding:0;box-sizing:border-box}
html,body{width:1149px;height:1200px;overflow:hidden}
body{font-family:"Lato",sans-serif;color:var(--text);
  background:radial-gradient(ellipse at 15% 45%,#dcdcdc 0,#efefef 35%,#fafafa 60%),#f5f5f5}
.page{position:relative;width:1149px;height:1200px}
.abs{position:absolute}
.frame-outer{left:174px;top:13px;width:801px;height:1100px;border:1px solid var(--frame);background:var(--white)}
.frame-inner{left:182px;top:20px;width:785px;height:1085px;border:1px solid var(--frame);background:var(--white)}

.logo{left:196px;top:40px;display:flex;align-items:center;gap:8px}
.logo-mark{width:50px;height:50px;border-radius:50%;background:var(--orange)}
.logo-name{font-weight:300;font-size:46px;line-height:46px;color:#3a3a3a;letter-spacing:-1px}
.logo-tag{left:253px;top:86px;font-size:9px;letter-spacing:.6px;color:#444}

.nav{left:539px;top:63px;display:flex;gap:21px;font-size:13px;color:#444}
.nav .active{color:var(--orange);font-weight:700}

.slider{left:198px;top:119px;width:754px;height:206px;
  background:linear-gradient(90deg,#1c2f6b 0%,#2a3f88 30%,#6b4a2c 55%,#d9762a 75%,#f3b04a 90%,#7a4a2a 100%)}
.slider-shadow{left:270px;top:320px;width:610px;height:30px;border-radius:50%;
  background:radial-gradient(ellipse at center,rgba(0,0,0,.35),rgba(0,0,0,0) 70%)}
.caption{left:231px;top:168px;width:275px;height:108px;border-radius:3px;background:rgba(240,240,240,.88);padding:14px 11px}
.caption h2{font-weight:400;font-size:18px;color:var(--orange);margin-bottom:6px}
.caption p{font-size:8.2px;line-height:14px;color:#222}
.btn-orange{display:inline-block;margin-top:8px;background:var(--orange);color:#fff;font-size:8.5px;font-weight:700;padding:3px 6px;border:1px solid #fff;outline:1px solid var(--orange)}
.arrow{width:22px;height:22px;border-radius:50%;background:var(--orange);border:2px solid #fff;box-shadow:0 0 2px rgba(0,0,0,.4)}
.dots{left:553px;top:294px;display:flex;gap:6px}
.dots span{width:10px;height:10px;border-radius:50%;background:#fff}
.dots span.on{background:transparent;border:2px solid #fff;box-shadow:inset 0 0 0 2px var(--orange)}

.intro h3{font-weight:400;font-size:18px;color:var(--ink);margin-bottom:18px}
.intro p{font-size:8.5px;line-height:13.6px;color:#222}

.card{width:237px}
.card .thumb{height:105px;border:1px solid #e3e3e3}
.card h4{font-weight:400;font-size:13.6px;color:var(--ink);margin:14px 0 16px -2px}
.card h4 em{font-style:normal;color:var(--orange)}
.card p{font-size:9.2px;line-height:11px;color:var(--muted);height:48px}
.btn-dark{display:inline-block;margin:13px 0 0 -2px;background:var(--charcoal);color:#fff;font-size:8.5px;font-weight:700;padding:3px 6px;box-shadow:0 2px 2px rgba(0,0,0,.25)}

.tab-more{left:958px;top:590px;width:22px;height:110px;background:var(--orange);border-radius:0 14px 14px 0;
  color:#fff;font-size:7.5px;font-weight:900;writing-mode:vertical-rl;text-align:center;line-height:22px}

.feed{left:198px;top:783px;width:148px;height:195px;background:var(--charcoal)}
.feed-box{position:absolute;left:3px;top:3px;width:140px;height:160px;background:#fff;padding:9px 16px 0 9px;overflow:hidden}
.feed-head{display:flex;align-items:center;gap:6px;font-size:8px;color:#555;margin-bottom:10px}
.feed-head i{width:14px;height:14px;border-radius:50%;background:var(--orange)}
.tweet{font-size:5.8px;line-height:8px;color:#888;margin-bottom:9px}
.tweet b{color:#222}
.tweet .meta{color:#222}
.feed-scroll{position:absolute;right:2px;top:6px;width:6px;height:150px;border-left:1px solid #ddd}
.feed-foot{position:absolute;left:7px;bottom:9px;font-size:8px;color:#fff;display:flex;align-items:center;gap:5px}
.feed-foot i{width:12px;height:12px;border-radius:50%;background:#fff}

.testi{left:356px;top:783px;width:372px;height:195px;background:var(--charcoal);color:#fff;padding:10px 12px}
.testi h3{font-weight:400;font-size:16px;margin-bottom:11px}
.testi p{font-size:8.7px;line-height:11px;width:236px}
.testi hr{border:0;border-top:1px solid #aaa;width:180px;margin:11px 0 12px}
.diff{position:absolute;left:262px;top:13px;width:100px;height:164px;border:1px solid #e26a3a;border-radius:8px;overflow:hidden}
.diff .photo{height:118px;background:linear-gradient(160deg,#1b2a57,#5d5f86 45%,#d8c8a0 60%,#2a2a3a)}
.diff .label{height:46px;background:linear-gradient(#f05a2a,#d8441a);padding:5px 7px;line-height:1}
.diff .label span{font-size:11px}
.diff .label strong{display:block;font-size:17px;font-weight:900;margin-top:2px}

.visit{left:738px;top:783px;width:213px;height:195px;
  background:linear-gradient(150deg,#3b4c6a 0%,#7b7e85 35%,#d6892a 55%,#4c3a2e 80%,#2a2a2a 100%);color:#fff}
.visit .cta{position:absolute;left:13px;bottom:12px}
.visit strong{display:block;font-size:21px;font-weight:900;line-height:22px;text-shadow:0 1px 2px rgba(0,0,0,.5)}
.visit span{font-size:12px;text-shadow:0 1px 2px rgba(0,0,0,.5)}

.band{left:196px;top:993px;width:755px;height:88px;background:var(--orange);color:#fff;overflow:hidden}
.band h3{position:absolute;left:11px;top:6px;font-size:18px;font-weight:400;color:#1a1a1a}
.band h3 b{color:#fff;font-weight:900}
.band .q{position:absolute;left:12px;top:32px;font-size:8.3px;font-weight:700;color:#1a1a1a}
.band .q2{position:absolute;left:12px;top:44px;font-size:8.3px;color:#1a1a1a}
.band .q2 b{color:#fff}
.band .calc-btn{position:absolute;left:12px;top:61px;background:var(--charcoal);font-size:8.3px;font-weight:700;padding:4px 6px}
.band .divider{position:absolute;left:515px;top:8px;width:1px;height:80px;background:#fff;opacity:.8}
.band h4{position:absolute;left:541px;top:8px;font-size:18px;font-weight:900}
.social{position:absolute;left:535px;top:34px;display:flex;gap:5px}
.social i{width:43px;height:43px;border-radius:50%;background:#fff}

.foot-nav{left:0;top:1124px;width:1149px;display:flex;justify-content:center;gap:22px;font-family:"Arimo",sans-serif;font-size:9.5px;color:#111}
.foot-nav .sep{color:#111}
.copy{left:0;top:1141px;width:1149px;text-align:center;font-family:"Arimo",sans-serif;font-size:7.5px;color:#222}
</style>
</head>
<body>
<div class="page">
  <div class="abs frame-outer"></div>
  <div class="abs frame-inner"></div>

  <header>
    <div class="abs logo"><i class="logo-mark"></i><span class="logo-name">Corvella</span></div>
    <div class="abs logo-tag">ROBOTIC WELDING TECHNOLOGIE</div>
    <nav class="abs nav">
      <span class="active">Home</span><span>About us</span><span>Competence</span><span>Case Story</span><span>Products</span><span>Videos</span>
    </nav>
  </header>

  <section>
    <div class="abs slider-shadow"></div>
    <div class="abs slider" role="img" aria-label="Robotic welding torch on a steel plate with bright sparks"></div>
    <div class="abs caption">
      <h2>Corvella</h2>
      <p>Lorem Ipsum is simply dummy text of the printing and typesetting industry. Lorem Ipsum has been the industry's standard</p>
      <span class="btn-orange">READ MORE</span>
    </div>
    <div class="abs arrow" style="left:187px;top:211px">
      <svg width="18" height="18" viewBox="0 0 18 18"><path d="M10.5 5 6.5 9l4 4" stroke="#fff" stroke-width="2" fill="none"/></svg>
    </div>
    <div class="abs arrow" style="left:940px;top:211px">
      <svg width="18" height="18" viewBox="0 0 18 18"><path d="M7.5 5l4 4-4 4" stroke="#fff" stroke-width="2" fill="none"/></svg>
    </div>
    <div class="abs dots"><span class="on"></span><span></span><span></span></div>
  </section>

  <section class="abs intro" style="left:200px;top:349px;width:364px">
    <h3>Welcome to Corvella.</h3>
    <p>Lorem Ipsum is simply dummy text of the printing and typesetting industry. Lorem Ipsum has been the industry's standard dummy text ever since the 1500s, when an unknown printer took a galley of type and scrambled it to make a type specimen book. It has survived not only five centuries, but also the leap into electronic typesetting, remaining essentially unchanged. It was popularised in the 1960s with the release of Typeset sheets containing Lorem Ipsum passages, and more recently with desktop publishing software like Layoutmaker including versions of Lorem Ipsum.</p>
  </section>
  <section class="abs intro" style="left:585px;top:349px;width:364px">
    <h3 style="margin-left:2px">About us</h3>
    <p>Lorem Ipsum is simply dummy text of the printing and typesetting industry. Lorem Ipsum has been the industry's standard dummy text ever since the 1500s, when an unknown printer took a galley of type and scrambled it to make a type specimen book.</p>
    <p style="margin-top:13.6px">&nbsp;It has survived not only five centuries, but also the leap into electronic typesetting, remaining essentially unchanged. It was popularised in the 1960s with the release of Typeset sheets containing Lorem Ipsum passages, and more recently with desktop publishing software like Layoutmaker including versions of Lorem Ipsum.</p>
  </section>

  <section>
    <article class="abs card" style="left:199px;top:525px">
      <div class="thumb" role="img" aria-label="Orange tinted industrial welding robot arm" style="background:linear-gradient(#f58a66,#f07850);display:flex;align-items:center;justify-content:center">
        <svg width="34" height="34" viewBox="0 0 34 34"><circle cx="13" cy="13" r="10" fill="#fff" stroke="#e0562a" stroke-width="2"/><path d="M13 8v10M8 13h10" stroke="#f15a29" stroke-width="2.5"/><path d="M20 20l9 9" stroke="#fff" stroke-width="4" stroke-linecap="round"/></svg>
      </div>
      <h4>General <em>Features</em></h4>
      <p>Lorem Ipsum has been the industry's standard dummy text ever since the 1500s, when an unknown printer took a galley of type and scrambled it to make a type specimen book</p>
      <span class="btn-dark">LEARN MORE</span>
    </article>
    <article class="abs card" style="left:456px;top:525px">
      <div class="thumb" role="img" aria-label="Mini crawler welding robot on a rail" style="background:linear-gradient(170deg,#d8d8d8,#b9b9b9 40%,#e8e6b0 60%,#6b6b7a)"></div>
      <h4>Mini Crawler <em>Welding Robot</em></h4>
      <p>Lorem Ipsum has been the industry's standard dummy text ever since the 1500s, when an unknown printer took a galley of type and scrambled it to make a type specimen book</p>
      <span class="btn-dark">LEARN MORE</span>
    </article>
    <article class="abs card" style="left:714px;top:525px">
      <div class="thumb" role="img" aria-label="Gantry welding robot in a workshop" style="background:linear-gradient(180deg,#b7b7b4,#3f5a86 45%,#20304f 75%,#585858)"></div>
      <h4>Gantry Welding <em>Robot</em></h4>
      <p>Lorem Ipsum has been the industry's standard dummy text ever since the 1500s, when an unknown printer took a galley of type and scrambled it to make a type specimen book</p>
      <span class="btn-dark">LEARN MORE</span>
    </article>
    <div class="abs tab-more">MORE PRODUCTS</div>
  </section>

  <section>
    <aside class="abs feed">
      <div class="feed-box">
        <div class="feed-head"><i></i>Corvella</div>
        <div class="tweet"><b>Corvella</b> I posted a new photo<br>to our page, see the update<br><span class="meta">58 days ago · reply · retweet · favorite</span></div>
        <div class="tweet"><b>Corvella</b> I posted a new photo<br>to our page, see the update<br><span class="meta">58 days ago · reply · retweet · favorite</span></div>
        <div class="tweet"><b>Corvella</b> I posted a new photo<br>to our page, see the update<br><span class="meta">58 days ago · reply · retweet · favorite</span></div>
        <div class="tweet"><b>Corvella</b> I posted a new photo<br>to our page, see the update<br><span class="meta">58 days ago · reply · retweet · favorite</span></div>
        <div class="feed-scroll"></div>
      </div>
      <div class="feed-foot"><i></i>Join the conversation</div>
    </aside>

    <div class="abs testi">
      <h3>Testimonails</h3>
      <p>“ Lorem Ipsum has been the industry's standard dummy text ever since the 1500s, when an unknown printer took a galley of type and scrambled it to make a type specimen book. ”</p>
      <hr>
      <p>“ Lorem Ipsum has been the industry's standard dummy text ever since the 1500s, when an unknown printer took a galley of type and scrambled it to make a type specimen book. Lorem Ipsum has been the industry's standard dummy text ever since the 1500s, when an unknown printer took a galley of type and scrambled it to make a type specimen book.”</p>
      <div class="diff">
        <div class="photo" role="img" aria-label="Welding sparks over a workpiece"></div>
        <div class="label"><span>What makes us</span><strong>Different?</strong></div>
      </div>
    </div>

    <div class="abs visit" role="img" aria-label="Orange robotic welding arm working with sparks">
      <div class="cta"><strong>Click here now to</strong><span>book your free site visit</span></div>
    </div>
  </section>

  <section class="abs band">
    <h3>Online <b>Free Estimate Calculator</b></h3>
    <div class="q">No sure of budget? Or Price Range of options?</div>
    <div class="q2">Find out immediately how much the Corvella you want will cost...<b>more</b></div>
    <span class="calc-btn">Free Estimate Calculator</span>
    <svg class="abs" style="left:400px;top:4px" width="80" height="90" viewBox="0 0 80 90">
      <g transform="rotate(15 40 45)">
        <rect x="18" y="8" width="46" height="82" rx="7" fill="#fff"/>
        <rect x="25" y="15" width="32" height="13" rx="2" fill="#f15a29"/>
        <g fill="#f15a29">
          <circle cx="30" cy="40" r="3.5"/><circle cx="41" cy="40" r="3.5"/><circle cx="52" cy="40" r="3.5"/>
          <circle cx="30" cy="52" r="3.5"/><circle cx="41" cy="52" r="3.5"/><circle cx="52" cy="52" r="3.5"/>
          <circle cx="30" cy="64" r="3.5"/><circle cx="41" cy="64" r="3.5"/><circle cx="52" cy="64" r="3.5"/>
        </g>
      </g>
    </svg>
    <div class="divider"></div>
    <h4>Follow us on</h4>
    <div class="social"><i></i><i></i><i></i></div>
  </section>

  <footer>
    <nav class="abs foot-nav">
      <span>HOME</span><span class="sep">I</span><span>ABOUT US</span><span class="sep">I</span><span>COMPETENCE</span><span class="sep">I</span><span>CASE STORY</span><span class="sep">I</span><span>PRODUCTS</span><span class="sep">I</span><span>VIDEOS</span>
    </nav>
    <div class="abs copy">Web Design by Brightline Studio © 2014 Corvella. All rights reserved.</div>
  </footer>
</div>
</body>
</html>
```